Wolkenfeld - a property developer - Website design

Hi all!
Exciting new project for you! :)
We are looking for some creative/modern designs to best represent us as a company.
Please have a look at the following link: huhu.wolkenfeld.eu to get an idea about who we are and what we do.
The 'Main Page' of the HP should be neatly arranged, easy to navigate, contain several pictures (changing every 10 seconds or so) that should reflect that we are property developers.
The navigation points ('About us', 'Projects' 'Investment', 'Contact Us', 'Legal Notice') should be included in the Design (again under every navigation point, pictures may be added - that reflect our profession and/or the subsection)
What we will need at the end of the day is a fully functional site - i.e: a site that is designed and programmed with backend/wordpress, to allow us to make changes anytime we feel like it.
Further questions?! Don't hesitate to contact me! Thanks :)
Target Market(s)
Real Estate Development/Building sector
Industry/Entity Type
Real Estate Development
Number of Pages Required
5+ page
Look and feel

```html
<!DOCTYPE html>
<html lang="en">
<head>
<meta charset="utf-8">
<title>Wolkenfeld – Property Developer</title>
<link href="https://fonts.googleapis.com/css2?family=Aldrich&family=Open+Sans:wght@400;600;700&display=swap" rel="stylesheet">
<style>
:root{
  --maroon:#4a1530;
  --maroon-dark:#3a0f25;
  --maroon-accent:#5e1d3e;
  --green:#8dc63f;
  --green-btn:#5fa61e;
  --ink:#333;
  --grey-text:#555;
  --light-bg:#e9e9e9;
  --header-bg:#ececec;
  --footer-bg:#333;
  --footer-bottom:#1c1c1c;
  --white:#fff;
  --head-font:'Aldrich',sans-serif;
  --body-font:'Open Sans',sans-serif;
}
*{box-sizing:border-box;margin:0;padding:0}
html,body{width:1200px;height:2214px;overflow:hidden}
body{position:relative;font-family:var(--body-font);color:var(--ink);background:var(--white)}
.abs{position:absolute}

/* header */
.site-header{left:0;top:0;width:1200px;height:78px;background:var(--header-bg)}
.brand{left:100px;top:14px;display:flex;align-items:center;gap:8px}
.brand-square{width:26px;height:48px;background:var(--maroon)}
.brand-name{font-family:var(--head-font);font-size:34px;color:var(--maroon);line-height:1}
.brand-sub{font-family:var(--head-font);font-size:10px;color:var(--maroon);margin-top:2px}
.social-top{left:873px;top:26px;display:flex;gap:7px}
.social-top span{width:26px;height:26px;background:#8a8a8a;display:block}
.lang{left:1012px;top:25px;width:88px;height:28px;background:var(--white);border:1px solid #d4d4d4;font-size:11px;line-height:26px;padding-left:26px;color:#444}
.lang::before{content:"";position:absolute;left:7px;top:9px;width:15px;height:9px;background:#3a4f8c}
.lang::after{content:"";position:absolute;right:9px;top:12px;border:4px solid transparent;border-top-color:#555}

/* nav */
.main-nav{left:0;top:78px;width:1200px;height:44px;background:var(--maroon)}
.main-nav ul{list-style:none;display:flex;position:absolute;left:100px;top:0;height:44px}
.main-nav li{color:var(--white);font-size:14.5px;font-weight:600;line-height:44px;padding:0 28px}
.main-nav li.active{background:var(--maroon-accent)}
.call{left:897px;top:78px;height:44px;line-height:44px;color:var(--white);font-size:9px}
.call strong{font-size:21px;font-weight:400;font-style:italic;margin-left:8px;vertical-align:-3px}

/* hero */
.hero{left:0;top:122px;width:1200px;height:424px;background:linear-gradient(100deg,#35506d 0%,#4a6a8a 45%,#2f3f54 100%)}
.hero-photo{position:absolute;inset:0}
.hero-title{left:125px;top:270px;font-family:var(--head-font);font-size:33px;line-height:42px;color:var(--white);font-weight:400}
.hero-arrow{top:186px;width:34px;height:34px;background:#222;border-radius:3px}
.hero-arrow svg{display:block}

/* welcome */
.welcome-title{left:100px;top:585px;font-family:var(--head-font);font-size:30px;color:#555;font-weight:400}
.welcome-title b{color:var(--maroon);font-weight:400}
.welcome-art{left:104px;top:640px;width:84px;height:172px;background:linear-gradient(180deg,#9a9a9a,#858585)}
.welcome-text{left:208px;top:638px;width:462px;font-size:11.5px;line-height:18px;color:#444}
.welcome-text p{margin-bottom:8px}
.welcome-text .more{font-weight:600;color:#333}
.welcome-photo{left:738px;top:597px;width:364px;height:219px;background:linear-gradient(180deg,#7fa6cf 0%,#c9d8e6 55%,#6e8f4a 100%);box-shadow:0 8px 10px -6px rgba(0,0,0,.35)}

/* features */
.features{left:0;top:862px;width:1200px;height:232px;background:var(--green)}
.feature{top:0;width:220px;text-align:center;color:var(--white)}
.feature svg{display:block;margin:43px auto 0}
.feature h3{font-size:16px;font-weight:600;margin-top:16px}
.feature p{font-size:11px;line-height:17.5px;margin-top:6px;opacity:.95}

/* projects */
.projects{left:0;top:1094px;width:1200px;height:551px;background:var(--light-bg)}
.section-title{width:1200px;left:0;text-align:center;font-family:var(--head-font);font-size:30px;color:#555;font-weight:400}
.section-title b{color:var(--maroon);font-weight:400}
.divider{left:495px;width:210px;height:1px;background:#bbb}
.divider::after{content:"";position:absolute;left:99px;top:-3px;width:12px;height:6px;border:1px solid #bbb;border-radius:3px;background:var(--light-bg)}
.projects-intro{left:0;top:1204px;width:1200px;text-align:center;font-size:13px;color:#666}
.grid{left:99px;top:1257px;width:1002px;height:345px;display:grid;grid-template-columns:repeat(4,1fr);grid-template-rows:repeat(2,1fr)}
.tile{position:relative}
.tile-overlay{position:absolute;left:17px;top:22px;width:216px;height:130px;border:1px solid rgba(255,255,255,.8);color:var(--white);text-align:center;font-size:12px}
.tile-overlay h4{font-size:12.5px;font-weight:600;margin-top:42px}
.tile-overlay hr{width:70px;border:0;border-top:1px solid #fff;margin:5px auto 10px}

/* partners */
.partner{top:1763px;width:231px;height:103px;border:1px solid #ddd;background:#fafafa;display:flex;align-items:center;justify-content:center;gap:10px;font-size:20px;font-weight:600;color:#444}
.partner i{width:22px;height:22px;display:block}
.footer-shadow{left:240px;top:1895px;width:720px;height:14px;background:radial-gradient(ellipse at center,rgba(0,0,0,.35),rgba(0,0,0,0) 70%)}

/* footer */
.site-footer{left:0;top:1910px;width:1200px;height:260px;background:var(--footer-bg);color:#ddd}
.f-col{top:55px}
.f-col h4{font-family:var(--head-font);font-size:17px;color:var(--white);font-weight:400;padding-bottom:6px;border-bottom:1px solid #4a4a4a}
.quick ul{list-style:none;margin-top:12px}
.quick li{font-size:11px;font-weight:600;line-height:24px;color:var(--white)}
.quick li::before{content:"›";margin-right:8px;color:#aaa}
.contact ul{list-style:none;margin-top:12px}
.contact li{display:flex;gap:12px;font-size:11.5px;line-height:17px;margin-bottom:9px;color:#ddd}
.contact li svg{flex:none;margin-top:2px}
.newsletter p{font-size:11.5px;line-height:17px;margin-top:12px;width:200px}
.newsletter .email{margin-top:12px;width:206px;height:30px;background:var(--white);font-size:10px;font-style:italic;color:#888;padding:0 8px;line-height:30px}
.newsletter .btn{margin-top:12px;width:98px;height:28px;background:var(--green-btn);color:var(--white);font-size:12px;font-weight:700;text-align:center;line-height:28px}
.f-brand{left:907px;top:95px;display:flex;align-items:center;gap:6px}
.f-brand .sq{width:18px;height:36px;background:#ddd}
.f-brand .n{font-family:var(--head-font);font-size:29px;color:#eee;line-height:1}
.social-foot{left:938px;top:168px;display:flex;gap:7px}
.social-foot span{width:26px;height:26px;display:block;border-radius:2px}
.bottom-bar{left:0;top:2170px;width:1200px;height:44px;background:var(--footer-bottom);color:#ddd;font-size:11px;line-height:44px;padding-left:100px}
</style>
</head>
<body>

<header class="abs site-header">
  <div class="abs brand">
    <div class="brand-square"></div>
    <div>
      <div class="brand-name">WOLKENFELD</div>
      <div class="brand-sub">Wolkenfeld-Immo.eu</div>
    </div>
  </div>
  <div class="abs social-top"><span></span><span></span><span></span><span></span></div>
  <div class="abs lang">English</div>
</header>

<nav class="abs main-nav">
  <ul>
    <li class="active">Home</li>
    <li>About us</li>
    <li>Projects</li>
    <li>Investment</li>
    <li>Legal Notice</li>
    <li>Contact Us</li>
  </ul>
</nav>
<div class="abs call">call us today <strong>+43 1555 0190</strong></div>

<section class="abs hero">
  <div class="hero-photo" role="img" aria-label="Businessman in a suit holding a small model house on his palm"></div>
  <div class="abs hero-arrow" style="left:15px">
    <svg width="34" height="34"><path d="M20 11 L12 17 L20 23 Z" fill="none" stroke="#fff" stroke-width="1.5"/></svg>
  </div>
  <div class="abs hero-arrow" style="left:1135px">
    <svg width="34" height="34"><path d="M14 11 L22 17 L14 23 Z" fill="none" stroke="#fff" stroke-width="1.5"/></svg>
  </div>
  <h1 class="abs hero-title">Helping You Find The<br>Property Of Your Dreams</h1>
</section>

<h2 class="abs welcome-title">Welcome to <b>Wolkenfeld</b></h2>
<div class="abs welcome-art" role="img" aria-label="Grey illustration of an apartment building"></div>
<div class="abs welcome-text">
  <p>Lorem ipsum dolor sit amet, consectetur adipiscing elit. Curabitur lobortis, tellus in aliquam cursus, ante lorem tristique elit, at aliquet nunc ante et orci.</p>
  <p>It is a long established fact that a reader will be distracted by the readable content of a page when looking at its layout. The point of using Lorem Ipsum is that it has a more-or-less normal distribution of letters, as opposed to using 'Content here, content here', making it look like readable English. Many desktop publishing packages and web page editors now use Lorem Ipsum as their default model text, and a search for 'lorem ipsum' will uncover many web sites still in their infancy. Various versions</p>
  <div class="more">More More »</div>
</div>
<div class="abs welcome-photo" role="img" aria-label="Modern white multi-storey villa with balconies on a green lawn"></div>

<section class="abs features">
  <div class="abs feature" style="left:95px">
    <svg width="54" height="54" viewBox="0 0 54 54" fill="none" stroke="#fff" stroke-width="2.5"><circle cx="33" cy="12" r="8"/><path d="M20 52 V34 a13 13 0 0 1 26 0 V52"/><path d="M4 30 L14 22 L24 30 V42 H4 Z"/></svg>
    <h3>New Projects</h3>
    <p>Lorem Ipsum is simply dummy text of the printing and typesetting industry.</p>
  </div>
  <div class="abs feature" style="left:358px">
    <svg width="54" height="54" viewBox="0 0 54 54" fill="#fff"><rect x="4" y="2" width="2.5" height="50"/><rect x="4" y="49.5" width="48" height="2.5"/><rect x="12" y="38" width="6" height="10"/><rect x="21" y="32" width="6" height="16"/><rect x="30" y="26" width="6" height="22"/><rect x="39" y="20" width="6" height="28"/><path d="M10 30 L40 8" stroke="#fff" stroke-width="2.5"/><path d="M34 6 L44 5 L41 14 Z"/></svg>
    <h3>case study</h3>
    <p>There are many variations of passages of Lorem Ipsum available, but the majority</p>
  </div>
  <div class="abs feature" style="left:621px">
    <svg width="54" height="54" viewBox="0 0 54 54" fill="#fff"><circle cx="15" cy="8" r="6"/><circle cx="39" cy="8" r="6"/><path d="M7 18 H23 L30 30 L24 33 L20 27 V52 H10 V27 Z"/><path d="M47 18 H31 L24 30 L30 33 L34 27 V52 H44 V27 Z"/></svg>
    <h3>Projects Development</h3>
    <p>Contrary to popular belief, Lorem Ipsum is not simply random text. It has roots in a piece</p>
  </div>
  <div class="abs feature" style="left:884px">
    <svg width="54" height="54" viewBox="0 0 54 54" fill="#fff"><path d="M27 4 L52 26 L48 30 L27 12 L6 30 L2 26 Z"/><path d="M12 30 L27 17 L42 30 V50 H12 Z"/><circle cx="27" cy="35" r="6" fill="#8dc63f"/></svg>
    <h3>Effective Price</h3>
    <p>Lorem Ipsum is that it has a more-or-less normal distribution of letters, as opposed to</p>
  </div>
</section>

<section class="abs projects"></section>
<h2 class="abs section-title" style="top:1128px">Our <b>Projects</b></h2>
<div class="abs divider" style="top:1175px"></div>
<p class="abs projects-intro">Lorem ipsum dolor sit amet, consectetur adipisicing elit. Culpa, alias enim placeat earum quos ab.</p>
<div class="abs grid">
  <div class="tile" style="background:linear-gradient(160deg,#4b5566,#6f7886)" role="img" aria-label="Modern office building facade">
    <div class="tile-overlay"><h4>View more</h4><hr>Lorem ipsum dolor sit amet,<br>consectetur adipisicing elit</div>
  </div>
  <div class="tile" style="background:linear-gradient(180deg,#6fa3d6,#a9c7e0 55%,#5d7f4c)" role="img" aria-label="City skyline with towers and a fountain"></div>
  <div class="tile" style="background:linear-gradient(180deg,#9fb3c4,#45484c 55%,#2d2e30)" role="img" aria-label="Contemporary house at dusk with lit garage"></div>
  <div class="tile" style="background:linear-gradient(180deg,#5d93d1,#b7cfe3 55%,#3f7a3a)" role="img" aria-label="Residential tower with pool and palm trees"></div>
  <div class="tile" style="background:linear-gradient(180deg,#dfe5ea,#8f9a86 55%,#4d7a32)" role="img" aria-label="Townhouses with green roofs on a lawn"></div>
  <div class="tile" style="background:linear-gradient(180deg,#8fb4d8,#d6dce0 55%,#6f8a52)" role="img" aria-label="High-rise apartment blocks under a blue sky"></div>
  <div class="tile" style="background:linear-gradient(180deg,#9eb9d4,#c8b69a 50%,#6d7f54)" role="img" aria-label="Suburban family house with double garage"></div>
  <div class="tile" style="background:linear-gradient(180deg,#f2f2f2,#4e6d96 45%,#8a6e55)" role="img" aria-label="Model of a blue house with brown roof on blueprints"></div>
</div>

<h2 class="abs section-title" style="top:1686px;font-size:26px">Wolkenfeld Is A Joint Venture Between</h2>
<div class="abs divider" style="top:1732px"></div>
<div class="abs partner" style="left:99px"><i style="background:#d0312d"></i>Stern Property</div>
<div class="abs partner" style="left:356px">Halden Group</div>
<div class="abs partner" style="left:612px"><i style="background:#1f7f9a;border-radius:50%"></i>Corvina Estates</div>
<div class="abs partner" style="left:870px;color:#1f4e8c">Brightledger</div>
<div class="abs footer-shadow"></div>

<footer class="abs site-footer">
  <div class="abs f-col quick" style="left:100px;width:135px">
    <h4>Quick Links</h4>
    <ul><li>Home</li><li>About Us</li><li>Projects</li><li>Investment</li><li>Legal Notice</li><li>Contact Us</li></ul>
  </div>
  <div class="abs f-col contact" style="left:311px;width:270px">
    <h4>Contact Information</h4>
    <ul>
      <li><svg width="12" height="14" viewBox="0 0 12 14"><path d="M6 0a5 5 0 0 1 5 5c0 4-5 9-5 9S1 9 1 5a5 5 0 0 1 5-5z" fill="#ddd"/><circle cx="6" cy="5" r="2" fill="#333"/></svg>Sonnweg 7/TOP 4B 1220 Vienna<br>- Austria</li>
      <li><svg width="12" height="12" viewBox="0 0 12 12"><path d="M2 0 L5 3 L3.5 5 A8 8 0 0 0 7 8.5 L9 7 L12 10 L10 12 A10 10 0 0 1 0 2 Z" fill="#ddd"/></svg><span><b>Phone:</b> +43 1555 0190</span></li>
      <li><svg width="12" height="12" viewBox="0 0 12 12"><rect x="3" y="0" width="6" height="4" fill="#ddd"/><rect x="0" y="4" width="12" height="5" fill="#ddd"/><rect x="3" y="8" width="6" height="4" fill="#ddd"/></svg><span><b>Fax:</b> +43 1555 0191</span></li>
      <li><svg width="13" height="10" viewBox="0 0 13 10"><rect x=".5" y=".5" width="12" height="9" fill="none" stroke="#ddd"/><path d="M.5 .5 L6.5 5.5 L12.5 .5" fill="none" stroke="#ddd"/></svg>info@wolkenfeld-immo.eu</li>
    </ul>
  </div>
  <div class="abs f-col newsletter" style="left:615px;width:205px">
    <h4>Newsletter Sign Up</h4>
    <p>Lorem ipsudolor sit coec adipiscin elitsite amet</p>
    <div class="email">Email Address</div>
    <div class="btn">SUBSCRIBE</div>
  </div>
  <div class="abs f-brand"><div class="sq"></div><div class="n">WOLKENFELD</div></div>
  <div class="abs social-foot">
    <span style="background:#3b5998"></span><span style="background:#1da1f2"></span><span style="background:#0e76a8"></span><span style="background:#f26522"></span>
  </div>
</footer>
<div class="abs bottom-bar">Copyright © 2015 Wolkenfeld-Immo.eu | All Right Reserved</div>

</body>
</html>
```